依頼概要
▽ターゲット
【■ 40~80歳■】向けの【■ ふとんの打ち直し■】販促用にポスターデザインを作成したいと考えており、デザイナー・クリエイターの方向けにコンペを開催いたします。

▽サイズ
【■A2サイズでトンボを付けて下さい。そのまま印刷屋に出せる形式(AIファイル必須■】

▽参考デザイン
サイト名:【■ ねむり堂川 ■】
参考URL:【■ http://www.nemuridokawa.co.jp/SHOP/582716/list.html■】

```html
<!DOCTYPE html>
<html lang="ja">
<head>
<meta charset="utf-8">
<title>わたふとん 仕立・打直し</title>
<link rel="stylesheet" href="https://fonts.googleapis.com/css2?family=M+PLUS+Rounded+1c:wght@800;900&family=Noto+Sans+JP:wght@500;700;900&display=swap">
<style>
:root{
  --red:#e60012;
  --white:#ffffff;
  --ink:#1a1a1a;
  --orange:#f08c1e;
  --yellow:#ffe600;
  --gray-box:#ececec;
  --frame:#bdbdbd;
}
*{margin:0;padding:0;box-sizing:border-box}
html,body{width:846px;height:1200px;overflow:hidden;background:var(--white)}
body{font-family:"Noto Sans JP",sans-serif;color:var(--ink)}
.poster{position:relative;width:846px;height:1200px;border:2px solid var(--frame);overflow:hidden}
.hero-block{position:absolute;left:79px;top:14px;width:682px;height:574px;background:var(--red)}
.hero-char{position:absolute;font-family:"M PLUS Rounded 1c",sans-serif;font-weight:900;color:var(--white);font-size:178px;line-height:1;width:190px;text-align:center}
.badge{position:absolute;border-radius:50%;background:var(--white);color:var(--red);font-family:"M PLUS Rounded 1c",sans-serif;font-weight:900;display:flex;align-items:center;justify-content:center}
.badge-shitate{left:42px;top:254px;width:172px;height:172px;font-size:58px}
.badge-uchinaoshi{left:488px;top:376px;width:180px;height:180px;font-size:52px}
.campaign{position:absolute;left:20px;top:548px;width:214px;height:150px}
.campaign-text{position:absolute;left:20px;top:548px;width:214px;height:150px;display:flex;flex-direction:column;align-items:center;justify-content:center;color:var(--red);font-weight:900;font-size:27px;line-height:1.15;transform:rotate(-12deg)}
.price-note{position:absolute;left:28px;top:670px;width:200px;font-size:15px;line-height:1.35;font-weight:500;text-align:center}
.price-list{position:absolute;left:268px;top:662px;list-style:none;font-weight:900;font-size:40px;line-height:54px;letter-spacing:0.5px}
.details{position:absolute;top:836px;width:394px}
.details-new{left:22px}
.details-common{left:432px}
.details-head{background:var(--orange);color:var(--white);font-weight:700;font-size:19px;height:32px;line-height:32px;padding-left:14px}
.details-list{list-style:none;margin-top:10px}
.details-list li{position:relative;padding-left:28px;font-size:21px;line-height:29px;font-weight:500;margin-bottom:4px}
.details-list li::before{content:"";position:absolute;left:4px;top:7px;width:16px;height:16px;border-radius:50%;background:var(--orange)}
.details-extra{font-size:20px;line-height:28px;font-weight:500;padding-left:10px}
.cotton-note{margin-top:12px;background:var(--gray-box);font-size:18px;line-height:27px;padding:6px 12px;font-weight:500}
.shop-bar{position:absolute;left:0;top:1106px;width:842px;height:80px;background:var(--yellow);display:flex;align-items:center;justify-content:center;gap:20px}
.shop-tag{font-size:22px;font-weight:700}
.shop-name{font-size:40px;font-weight:900}
</style>
</head>
<body>
<main class="poster">
  <div class="hero-block"></div>
  <span class="hero-char" style="left:560px;top:4px">わ</span>
  <span class="hero-char" style="left:560px;top:166px">た</span>
  <span class="hero-char" style="left:293px;top:52px">ふ</span>
  <span class="hero-char" style="left:293px;top:234px">と</span>
  <span class="hero-char" style="left:293px;top:416px">ん</span>

  <div class="badge badge-shitate">仕立</div>
  <div class="badge badge-uchinaoshi">打直し</div>

  <svg class="campaign" viewBox="0 0 214 150" aria-hidden="true">
    <polygon fill="var(--yellow)" points="107,4 122,28 148,12 150,40 180,34 170,60 206,66 180,84 204,106 170,108 176,138 146,124 132,148 110,128 88,146 76,120 44,134 46,106 10,100 36,80 8,58 44,54 38,24 68,34 78,8 94,28"/>
  </svg>
  <div class="campaign-text"><span>キャンペーン</span><span>実施中!!</span></div>

  <p class="price-note">表示価格は税込、<br>敷き布団に同じ価格です。</p>

  <ul class="price-list">
    <li>シングル……¥8,800～</li>
    <li>セミダブル…¥9,800～</li>
    <li>ダブル………¥10,800～</li>
  </ul>

  <section class="details details-new">
    <h2 class="details-head">新品の詳細について</h2>
    <ul class="details-list">
      <li>新品のお布団は上記各サイズより¥3,000UPでお造り致します。</li>
      <li>掛けの中綿は少し割高ですが米綿がおすすめです!</li>
    </ul>
    <p class="cotton-note">米綿の特徴は保湿性､吸湿性の高さに加え<br>しっとり体にFITします。</p>
  </section>

  <section class="details details-common">
    <h2 class="details-head">仕立て直し、新品共通の詳細について</h2>
    <ul class="details-list">
      <li>柄は『おまかせ』で男柄か女柄かをご選択ください。</li>
      <li>ロング丈(10cm長)は¥1,000UPで承ります。</li>
    </ul>
    <p class="details-extra">尚、枕やカバー等もご用意できます。<br>詳しくは店主まで</p>
  </section>

  <footer class="shop-bar">
    <span class="shop-tag">クリーニングと寝具の店</span>
    <span class="shop-name">ふとんの東山</span>
  </footer>
</main>
</body>
</html>
```